Web Design for Meadowfield Turf Crew

Meadowfield Turf Crew needs the photoshop files for a simple, clean and professional web design. I need a home and subpage design, although they can be very similar. See pagestridehub.com for a desired layout, although I'd like to see more design than shown on that site. The goal of the site is to attract both lawn maintenance/landscape customers and build a partner network of consultants that serve the US market. The following are needed:

- home and subpage design
- page: Home, Services, Locations, Consultants, FAQ, Contact
- if subpages have header photo, need to include 5 different header photos for each page
- favicon
Updates

I'll award the design based on the homepage concept. The minor subpage changes and other elements can be worked out in the workroom stage. Thanks, Trent

Industry/Entity Type

It Professional

```html
<!DOCTYPE html>
<html lang="en">
<head>
<meta charset="utf-8">
<title>Meadowfield Turf Crew</title>
<link href="https://fonts.googleapis.com/css2?family=Lato:wght@300;400&family=Montserrat:wght@500;700&family=Open+Sans:wght@600&family=Raleway:wght@400;500&display=swap" rel="stylesheet">
<style>
:root{
  --green:#6a9a1a;
  --green-bright:#7cb026;
  --ink:#3f434b;
  --text:#4a4d52;
  --muted:#a9abae;
  --page:#f4f5f6;
  --footer:#414650;
  --white:#ffffff;
  --logo-grey:#6b6d70;
}
*{box-sizing:border-box;margin:0;padding:0}
html,body{width:1165px;height:1200px;overflow:hidden}
body{position:relative;background:var(--page);font-family:'Lato',sans-serif;color:var(--text)}

.site-header{position:absolute;left:0;top:0;width:1165px;height:109px;background:var(--white)}
.brand{position:absolute;left:101px;top:30px;display:flex;align-items:center;gap:14px}
.brand-mark{width:56px;height:56px;border:4px solid var(--logo-grey);border-radius:6px}
.brand-name{font-family:'Lato',sans-serif;font-weight:400;font-size:23px;color:var(--logo-grey);line-height:1;border-left:2px solid var(--logo-grey);padding-left:14px;height:56px;display:flex;align-items:center;white-space:nowrap}
.main-nav{position:absolute;right:103px;top:66px;display:flex;gap:32px;font-family:'Raleway',sans-serif;font-size:14px;font-weight:500;letter-spacing:.3px}
.main-nav a{color:#555;text-decoration:none}
.main-nav a.active{color:var(--green-bright)}

.hero{position:absolute;left:0;top:109px;width:1165px;height:480px;
  background:radial-gradient(ellipse at 60% 10%,#c9d84a 0%,rgba(160,190,40,.4) 25%,transparent 55%),linear-gradient(180deg,#6c9a2c 0%,#5d8f24 35%,#76a534 65%,#84b23c 100%)}
.hero-title{position:absolute;top:155px;width:100%;text-align:center;font-family:'Montserrat',sans-serif;font-weight:700;font-size:46px;color:var(--white);letter-spacing:1px}
.hero-sub{position:absolute;top:232px;width:100%;text-align:center;font-family:'Open Sans',sans-serif;font-weight:600;font-size:17px;color:var(--white)}
.hero-btn{position:absolute;left:489px;top:296px;width:187px;height:64px;border:1px solid var(--white);border-radius:4px;display:flex;align-items:center;justify-content:center;font-family:'Montserrat',sans-serif;font-weight:500;font-size:16px;color:var(--white);letter-spacing:.3px}
.dots{position:absolute;top:418px;left:557px;display:flex;gap:10px}
.dots span{width:11px;height:11px;border-radius:50%;background:#86b83a}
.dots span.on{background:var(--white)}

.welcome{position:absolute;left:101px;top:626px;width:630px}
.welcome h1{font-weight:300;font-size:23px;color:#2f3135;white-space:nowrap}
.welcome h1 em{font-style:normal;color:var(--green-bright)}
.welcome p{margin-top:10px;font-size:14px;line-height:24px;text-transform:uppercase;color:#555}

.service{position:absolute;top:778px;width:314px}
.service .photo{height:127px}
.service h2{margin-top:18px;font-weight:400;font-size:22px;color:var(--green-bright)}
.service p{margin-top:8px;width:302px;font-size:14px;line-height:24px;color:#444}

.quick{position:absolute;left:750px;top:606px;width:314px;height:436px;background:var(--green);padding:16px 20px 0}
.quick h3{font-weight:400;font-size:19px;color:var(--white);text-transform:uppercase}
.field{display:block;margin-top:14px;margin-left:4px;width:270px;height:46px;background:var(--white);padding:15px 15px;font-size:14px;color:var(--muted)}
.quick h3 + .field{margin-top:15px}
.field.message{height:114px}
.send{margin-top:20px;margin-left:1px;width:100px;height:48px;background:var(--ink);color:var(--white);font-size:18px;display:flex;align-items:center;justify-content:center}

.site-footer{position:absolute;left:0;top:1068px;width:1165px;height:132px;background:var(--footer)}
.foot-nav{position:absolute;left:100px;top:28px;display:flex;gap:32px;font-family:'Raleway',sans-serif;font-size:14px;font-weight:500;color:var(--white)}
.copyright{position:absolute;left:100px;top:58px;font-family:'Raleway',sans-serif;font-size:14px;color:var(--white)}
.social{position:absolute;left:914px;top:56px;display:flex;gap:2px}
.social span{width:36px;height:36px;border-radius:50%;background:var(--white)}
</style>
</head>
<body>
<header class="site-header">
  <div class="brand"><div class="brand-mark"></div><div class="brand-name">Meadowfield Turf Crew</div></div>
  <nav class="main-nav">
    <a class="active">HOME</a><a>SERVICES</a><a>LOCATIONS</a><a>CONSULTANTS</a><a>FAQ</a><a>CONTACT</a>
  </nav>
</header>

<section class="hero" role="img" aria-label="Sunlit green meadow with rolling hills and a wooden fence">
  <div class="hero-title">LANDSCAPE SERVICES</div>
  <div class="hero-sub">TO PROVIDE VALUE FOR MONEY AND EXCELLENCE IN GROUNDS MAINTENANCE</div>
  <div class="hero-btn">VIEW OUR SERVICE</div>
  <div class="dots"><span class="on"></span><span></span><span></span></div>
</section>

<section class="welcome">
  <h1>WELCOME TO <em>MEADOWFIELD TURF CREW</em> SERVICES</h1>
  <p>Our commitment is to provide our customers with quality landscape construction and maintenance as well as friendly and responsive customer service.</p>
</section>

<article class="service" style="left:101px">
  <div class="photo" role="img" aria-label="Country road between a ploughed field and green grass" style="background:linear-gradient(180deg,#9fc3e6 0%,#d7e6f2 22%,#4f6a2a 26%,#8a6b4f 45%,#7b8f4a 75%,#5f9a2c 100%)"></div>
  <h2>lawn maintenance</h2>
  <p>Lorem ipsum dolor sit amet, consectetur adipisicing elit, sed do eiusmod tempor incididunt ut labore et dolore magna aliqua.</p>
</article>

<article class="service" style="left:425px">
  <div class="photo" role="img" aria-label="Freshly mown field under a cloudy sky" style="background:linear-gradient(180deg,#7fa7cf 0%,#c9d9e6 45%,#6d8a3a 58%,#8fa84a 78%,#6f9030 100%)"></div>
  <h2>landscape services</h2>
  <p>Lorem ipsum dolor sit amet, consectetur adipisicing elit, sed do eiusmod tempor incididunt ut labore et dolore magna aliqua.</p>
</article>

<aside class="quick">
  <h3>Quick Contact</h3>
  <div class="field">Enter Your Name</div>
  <div class="field">Enter Your Mail</div>
  <div class="field">Enter Your Phone Number</div>
  <div class="field message">Enter Your Message</div>
  <div class="send">SEND</div>
</aside>

<footer class="site-footer">
  <nav class="foot-nav"><span>HOME</span><span>SERVICES</span><span>LOCATIONS</span><span>CONSULTANTS</span><span>FAQ</span><span>CONTACT</span></nav>
  <div class="copyright">COPYRIGHT © 2014</div>
  <div class="social" aria-label="Social links"><span></span><span></span><span></span><span></span></div>
</footer>
</body>
</html>
```